Meridian Sound Wellness LLC Card Design

Need business card with a logo for a hearing aid sales and audiology business. We have two Hearing Instrument Specialists and one Audiologist on staff. Over 25 years in business. Locally owned and operated. Financing available. Most insurances accepted.

Meridian Sound Wellness LLC
48730 W Linden Row, Suite 9
Spokane, WA 99481
509-617-2085
www.meridiansoundnorth.example

Manager
Tobias Wrenfield HIS COHC
License #81729046

Target Market(s)

50yr old + people with a hearing loss.

Industry/Entity Type

Business

Contact Information for Business Card

48730 W Linden Row, Suite 9
Spokane, WA 99481
509-617-2085
www.meridiansoundnorth.example

Manager
Tobias Wrenfield HIS COHC
NRPL #81729046

Font styles to use
Serif
Sans Serif

Requirements
Must have
• Business name, Tobias's name and title(s) and contact information, License #, web address
Nice to have
Should not have

```html
<!DOCTYPE html>
<html lang="en">
<head>
<meta charset="utf-8">
<title>Meridian Sound Wellness – Business Card</title>
<link rel="stylesheet" href="https://fonts.googleapis.com/css2?family=Open+Sans:wght@400;600;700&display=swap">
<style>
  :root {
    --backdrop: #e9e6e2;
    --card-white: #ffffff;
    --brand-navy: #1c4693;
    --brand-blue: #1a6dbd;
    --ink: #2b2b2b;
    --rule: #b9b9b9;
    --photo-warm: #f3ece4;
    --photo-grey: #dcdcdc;
  }
  * { margin: 0; padding: 0; box-sizing: border-box; }
  html, body {
    width: 1200px; height: 1000px; overflow: hidden;
    background: var(--backdrop);
    font-family: "Open Sans", Arial, sans-serif;
    color: var(--ink);
  }
  .card {
    position: absolute; left: 265px; width: 665px; height: 397px;
    background: var(--card-white); border-radius: 22px; overflow: hidden;
    box-shadow: 0 6px 14px rgba(0,0,0,0.25);
  }
  .card-front { top: 73px; }
  .card-back { top: 532px; }

  .brand-name {
    position: absolute; color: var(--brand-navy);
    font-weight: 600; line-height: 1.05; letter-spacing: -0.5px;
  }
  .card-front .brand-name { left: 32px; top: 46px; font-size: 36px; }
  .card-back .brand-name { left: 305px; top: 250px; font-size: 36px; }
  .brand-name .brand-dot {
    display: inline-block; width: 14px; height: 14px; border-radius: 50%;
    background: var(--brand-navy); margin-right: 10px; vertical-align: 4px;
  }

  .contact { position: absolute; left: 33px; font-size: 16px; line-height: 1.3; }
  .contact-line { display: flex; align-items: center; gap: 7px; }
  .contact-line svg { width: 15px; height: 15px; fill: var(--brand-navy); }
  .contact-phone { top: 230px; }
  .contact-web { top: 254px; }
  .company { position: absolute; left: 33px; top: 285px; font-size: 16px; line-height: 21px; }
  .company strong { font-weight: 600; }

  .divider { position: absolute; left: 180px; top: 240px; width: 454px; height: 1px; background: var(--rule); }

  .person { position: absolute; right: 31px; top: 206px; text-align: right; font-size: 16px; }
  .person-name { color: var(--brand-navy); font-weight: 700; font-size: 20px; text-transform: uppercase; }
  .person-creds { color: var(--brand-blue); font-weight: 400; font-size: 16px; margin-left: 3px; }
  .person-role { margin-top: 16px; line-height: 26px; }

  .base-band { position: absolute; left: 0; bottom: 0; width: 665px; height: 23px; }

  .photo-area {
    position: absolute; inset: 0;
    background: linear-gradient(100deg, var(--photo-grey) 0%, var(--photo-warm) 35%, var(--card-white) 70%);
  }
</style>
</head>
<body>
  <section class="card card-front">
    <div class="brand-name"><span class="brand-dot"></span>Meridian Sound<br>Wellness</div>

    <div class="contact contact-phone contact-line">
      <svg viewBox="0 0 16 16" aria-hidden="true"><path d="M2 5c0-2 2-3 6-3s6 1 6 3v1h-3V5H5v1H2zM4 7h8l2 6H2z"/></svg>
      <span>509-617-2085</span>
    </div>
    <div class="contact contact-web contact-line">
      <svg viewBox="0 0 16 16" aria-hidden="true"><circle cx="8" cy="8" r="7"/><path d="M1 8h14M8 1c-3 4-3 10 0 14M8 1c3 4 3 10 0 14" stroke="#fff" stroke-width="1" fill="none"/></svg>
      <span>www.meridiansoundnorth.example</span>
    </div>
    <div class="divider"></div>

    <div class="company">
      <strong>Meridian Sound Wellness</strong> LLC<br>
      48730 W Linden Row, Suite 9<br>
      Spokane, WA 99481
    </div>

    <div class="person">
      <div><span class="person-name">Tobias Wrenfield</span><span class="person-creds">HIS COHC</span></div>
      <div class="person-role">Manager<br>License #81729046</div>
    </div>

    <svg class="base-band" viewBox="0 0 665 23" preserveAspectRatio="none" aria-hidden="true">
      <polygon points="0,0 340,0 318,23 0,23" fill="var(--brand-navy)"/>
      <polygon points="345,0 665,0 665,23 323,23" fill="var(--brand-blue)"/>
      <line x1="347" y1="0" x2="322" y2="23" stroke="#fff" stroke-width="2"/>
    </svg>
  </section>

  <section class="card card-back">
    <div class="photo-area" role="img" aria-label="Soft faded photo of an older person wearing glasses and a behind-the-ear hearing aid"></div>
    <div class="brand-name"><span class="brand-dot"></span>Meridian Sound<br>Wellness</div>
  </section>
</body>
</html>
```